Recrutering company needs a Roll-Up Design

We need a Roll-Up Design for our company, which is dedicated to personnel selection. We would like the roll-up to feature our logo and the silhouette of the buildings shown in one of the uploaded photos (the one called "CorbelloVistaUrte4"). Additionally, we'd like to incorporate the words "Persones," "Talent," and "Èxit" with shadows using the English equivalents instead of the original ones, so: "People" for "Persones," "Talent" for "Talent," and "Success" for "Èxit."

The color of the logo can be changed to red, and the overall design can incorporate this color. As the design is for a roll-up, its essential to take into account a 4cm margin.

```html
<!DOCTYPE html>
<html lang="ca">
<head>
<meta charset="utf-8">
<title>Roll-up – CorbelloVistaUrte4</title>
<link rel="stylesheet" href="https://fonts.googleapis.com/css2?family=Poppins:wght@400;500;700&display=swap">
<style>
  :root {
    --page-bg: #ebebeb;
    --night-top: #173566;
    --night-mid: #284f91;
    --night-low: #3a5ea6;
    --snow: #dfe6f2;
    --wine: #8a1a3a;
    --crimson: #b5214a;
    --crimson-bright: #c0234c;
    --rose-grey: #b08a97;
    --paper: #ffffff;
    --echo-grey: #bdbdbd;
    --echo-wine: #5e0f26;
    --white: #ffffff;
  }
  html, body {
    margin: 0;
    width: 746px;
    height: 1200px;
    overflow: hidden;
    background: var(--page-bg);
  }
  .rollup {
    position: absolute;
    left: 153px;
    top: 82px;
    width: 440px;
    height: 1036px;
    box-shadow: 0 6px 18px rgba(0,0,0,0.18);
  }
  .rollup svg { display: block; width: 100%; height: 100%; }
  .word {
    font-family: "Poppins", sans-serif;
    font-weight: 700;
    text-anchor: middle;
  }
  .word--light { fill: var(--white); }
  .word--crimson { fill: var(--crimson-bright); }
  .echo { font-family: "Poppins", sans-serif; font-weight: 700; text-anchor: middle; }
  .echo--wine { fill: var(--echo-wine); opacity: 0.55; }
  .echo--grey { fill: var(--echo-grey); }
  .brand-name {
    font-family: "Poppins", sans-serif;
    font-weight: 500;
    fill: var(--white);
    text-anchor: middle;
    letter-spacing: 0.5px;
  }
  .brand-tagline {
    font-family: "Poppins", sans-serif;
    font-weight: 500;
    fill: var(--white);
    text-anchor: middle;
    letter-spacing: 1.2px;
  }
  .site-address {
    font-family: "Poppins", sans-serif;
    font-weight: 400;
    fill: var(--white);
    text-anchor: middle;
  }
</style>
</head>
<body>
<div class="rollup">
  <svg viewBox="0 0 427 1005" xmlns="http://www.w3.org/2000/svg">
    <defs>
      <linearGradient id="night-sky" x1="0" y1="0" x2="0" y2="1">
        <stop offset="0" stop-color="var(--night-top)"/>
        <stop offset="0.6" stop-color="var(--night-mid)"/>
        <stop offset="0.85" stop-color="var(--night-low)"/>
        <stop offset="1" stop-color="var(--snow)"/>
      </linearGradient>
    </defs>

    <!-- paper base -->
    <rect class="paper" x="0" y="0" width="427" height="1005" fill="var(--paper)"/>

    <!-- night scene -->
    <rect class="night-scene" x="0" y="0" width="427" height="430" fill="url(#night-sky)"
          role="img" aria-label="Illustration of a starry night sky with a constellation and a snowy village of small houses and a lit building"/>

    <!-- brand -->
    <g class="brand">
      <circle cx="213.5" cy="60" r="9" fill="none" stroke="var(--white)" stroke-width="1.5"/>
      <text class="brand-name" x="213.5" y="100" font-size="14">CORBELLOVISTAURTE4</text>
      <text class="brand-tagline" x="213.5" y="114" font-size="7">SELECCIÓ DE TALENT</text>
    </g>

    <!-- red bands -->
    <polygon class="band-edge" points="0,414 427,364 427,372 0,422" fill="var(--crimson)"/>
    <polygon class="band-main" points="0,422 427,372 427,600 0,590" fill="var(--wine)"/>
    <polygon class="band-lower" points="0,590 427,600 427,622 0,652" fill="var(--crimson)"/>
    <polygon class="band-tint" points="230,628 427,598 427,640" fill="var(--rose-grey)"/>

    <!-- headline words -->
    <g class="headline">
      <text class="echo echo--wine" font-size="46" transform="translate(213.5 506) scale(1 -1.05)" x="0" y="0" dy="0">PEOPLE</text>
      <text class="word word--light" x="213.5" y="502" font-size="46">PERSONES</text>

      <text class="echo echo--grey" font-size="46" transform="translate(213.5 728) scale(1.08 -0.75)" x="0" y="0">TALENT</text>
      <text class="word word--crimson" x="213.5" y="724" font-size="46">TALENT</text>

      <text class="echo echo--grey" font-size="48" transform="translate(213.5 852) scale(1 -1.05)" x="0" y="0">SUCCESS</text>
      <text class="word word--crimson" x="213.5" y="848" font-size="46">ÈXIT</text>
    </g>

    <!-- footer -->
    <rect class="footer" x="0" y="940" width="427" height="65" fill="var(--crimson)"/>
    <text class="site-address" x="213.5" y="980" font-size="22">www.corbellovistaurte4.com</text>
  </svg>
</div>
</body>
</html>
```